Lucky Orbit Fun Casino Entertainment

Looking to update my business card and make it look more modern, stand out and eye catching.
We are are fun casino business in Australia (primarily Sydney). Blackjack and Roulette are our most popular games although we have pretty much every game available for hire that you would find in a real casino. The final design would need to be sleek and appeal to the more upmarket corporate sector.
We mainly cater for Corporate Events, Private Parties, Fundraising Events, Team Building, Poker Tournaments
I think I'd prefer the colour Black.

Target Market(s)

High-end Corporate

Industry/Entity Type

Events

Contact Information for Business Card

Dale Hutchins
Director
1300 482 617
0431 758 209
info@luckyorbit.com.au
www.luckyorbit.com.au
Facebook & Instagram @luckyorbitshows (proper social icons preferred)

Colors
000000
0255a3

Requirements
Must have
• Front side:
• Logo
• Contact details
• 'Australia's #1 Fun Casino Specialists'
• Back:
• Logo
Nice to have
• Back:
• Corporate Events
• Private Parties
• Poker Tournaments
• Fundraising
• Props & Theming
• Photo Booth
• Horse Racing Events
• The Vegas Sign attached, maybe on the back of the card in the background...?

```html
<!DOCTYPE html>
<html lang="en">
<head>
<meta charset="utf-8">
<title>Lucky Orbit – Business Card</title>
<link href="https://fonts.googleapis.com/css2?family=Montserrat:wght@500;600;700&display=swap" rel="stylesheet">
<style>
  :root{
    --bg:#2a2a2d;
    --card:#141414;
    --card-edge:#1c1c1c;
    --gold:#f6b21b;
    --blue:#2f8fd8;
    --white:#f2f2f2;
    --heart:#e02a2a;
    --ink:#111111;
  }
  *{margin:0;padding:0;box-sizing:border-box}
  html,body{width:1200px;height:800px;overflow:hidden}
  body{
    background:var(--bg);
    font-family:"Montserrat",Arial,sans-serif;
    display:flex;align-items:center;justify-content:center;gap:36px;
  }
  .card{
    position:relative;width:560px;height:320px;border-radius:18px;
    background:linear-gradient(160deg,var(--card-edge),var(--card));
    box-shadow:0 18px 40px rgba(0,0,0,.45);overflow:hidden;color:var(--white);
  }
  .brand{display:flex;align-items:center;gap:14px;white-space:nowrap}
  .brand-dot{width:54px;height:54px;border-radius:50%;background:var(--gold);flex:none}
  .brand-name{font-weight:700;font-size:40px;color:var(--gold);letter-spacing:1px;line-height:1}

  /* back side */
  .card--back .brand{position:absolute;left:50%;top:86px;transform:translateX(-50%)}
  .services{
    position:absolute;left:0;right:0;bottom:62px;text-align:center;
    font-size:14.5px;font-weight:500;line-height:1.75;
  }
  .services .sep{color:var(--heart);margin:0 5px}

  /* front side */
  .card--front .brand{position:absolute;left:34px;top:118px;gap:12px}
  .card--front .brand-dot{width:40px;height:40px}
  .card--front .brand-name{font-size:25px;letter-spacing:.5px}
  .divider{position:absolute;left:290px;top:34px;width:1px;height:200px;background:var(--gold)}
  .contact{position:absolute;left:312px;top:36px;font-size:13px;font-weight:500;line-height:1.5}
  .person-name{color:var(--gold);font-weight:700;font-size:17px;letter-spacing:.3px}
  .person-role{color:var(--blue);font-weight:600;font-size:14px;margin-bottom:8px}
  .address{margin-bottom:8px}
  .contact-line{display:flex;align-items:center;gap:8px;height:22px}
  .contact-line svg{width:17px;height:17px;flex:none}
  .tagline-band{
    position:absolute;left:0;right:0;bottom:22px;height:30px;background:var(--gold);
    color:var(--ink);font-weight:700;font-size:14px;letter-spacing:.4px;
    display:flex;align-items:center;justify-content:center;
  }
</style>
</head>
<body>

<section class="card card--back" aria-label="Card back">
  <div class="brand">
    <span class="brand-dot"></span>
    <span class="brand-name">LUCKY ORBIT</span>
  </div>
  <p class="services">
    Corporate Events<span class="sep">♥</span>Private Parties<span class="sep">♥</span>Poker Tournaments<span class="sep">♥</span>Fundraising<br>
    Props &amp; Theming<span class="sep">♥</span>Photo Booth<span class="sep">♥</span>Horse Racing Events
  </p>
</section>

<section class="card card--front" aria-label="Card front">
  <div class="brand">
    <span class="brand-dot"></span>
    <span class="brand-name">LUCKY ORBIT</span>
  </div>
  <div class="divider"></div>
  <div class="contact">
    <p class="person-name">DALE HUTCHINS</p>
    <p class="person-role">CEO/FOUNDER</p>
    <p class="address">18 Harbour Lane<br>Level 4, Sydney<br>NSW 2000</p>
    <p class="contact-line">
      <svg viewBox="0 0 20 20"><circle cx="10" cy="10" r="9" fill="none" stroke="var(--blue)" stroke-width="1.5"/><path d="M7 5.5l1.6 2.2-1 1.1a6 6 0 0 0 3.6 3.6l1.1-1 2.2 1.6-1 1.6c-3.8-.2-7.2-3.6-7.4-7.4z" fill="var(--blue)"/></svg>
      1300 482 617
    </p>
    <p class="contact-line">
      <svg viewBox="0 0 20 20"><circle cx="10" cy="10" r="9" fill="none" stroke="var(--blue)" stroke-width="1.5"/><rect x="7" y="4.5" width="6" height="11" rx="1.2" fill="var(--blue)"/><rect x="8.2" y="6" width="3.6" height="6.5" fill="var(--card)"/></svg>
      0431 758 209
    </p>
    <p class="contact-line">
      <svg viewBox="0 0 20 20"><circle cx="10" cy="10" r="9" fill="none" stroke="var(--blue)" stroke-width="1.5"/><rect x="5" y="6.5" width="10" height="7" rx="1" fill="var(--blue)"/><path d="M5.5 7l4.5 3.5L14.5 7" fill="none" stroke="var(--card)" stroke-width="1"/></svg>
      info@luckyorbit.com.au
    </p>
    <p class="contact-line">
      <svg viewBox="0 0 20 20"><circle cx="10" cy="10" r="9" fill="none" stroke="var(--blue)" stroke-width="1.5"/><circle cx="10" cy="10" r="5" fill="none" stroke="var(--blue)" stroke-width="1.2"/><ellipse cx="10" cy="10" rx="2.2" ry="5" fill="none" stroke="var(--blue)" stroke-width="1"/><path d="M5 10h10" stroke="var(--blue)" stroke-width="1"/></svg>
      www.luckyorbit.com.au
    </p>
  </div>
  <div class="tagline-band">AUSTRALIA'S #1 FUN CASINO SPECIALISTS</div>
</section>

</body>
</html>
```